CareRally482
Business Cards and Stationary
CareRally482 - Emergency Services
Creative Brief
Use specific fonts
Use fonts and colors from our new logo and website that are attached
Professional
Gordon P. Hartwell
Owner
20415 E Ridge Ave Suite 230-519 Harlow Springs, NM 85261
gph@carerally482.com
www.carerally482.com
Use uploaded website draft for colors and fonts, you can get an idea of what we do from the current website. NOTE: We will need business card templates for; Marlena J. Hartwell Owner cell (623) 555-0187 email marlena@carerally482.com Douglas R. Pembry DO Medical Director cell (602)555-0134 email dpembrydo@carerally482.com
open to great ideas

```html
<!DOCTYPE html>
<html lang="en">
<head>
<meta charset="utf-8">
<title>CareRally482 Stationery</title>
<link rel="stylesheet" href="https://fonts.googleapis.com/css2?family=Roboto:wght@400;700;900&display=swap">
<style>
:root{
  --bg:#9a9b9d;
  --paper:#ffffff;
  --blue:#1f4fb8;
  --blue-deep:#163c95;
  --blue-light:#3f74de;
  --ink:#4b4d52;
  --grey-line:#c3c6cc;
  --silver-a:#f4f4f5;
  --silver-b:#c9cbcf;
  --ghost:#e6ebf5;
}
*{margin:0;padding:0;box-sizing:border-box}
html,body{width:1200px;height:821px;overflow:hidden;background:var(--bg);font-family:"Roboto",Arial,sans-serif;color:var(--ink)}
.canvas{position:relative;width:1200px;height:821px}
.sheet{position:absolute;background:var(--paper);overflow:hidden;box-shadow:0 2px 6px rgba(0,0,0,.25)}
.brand{font-family:"Roboto",Arial,sans-serif;font-weight:900;color:var(--ink);white-space:nowrap;letter-spacing:.5px}
.brand--white{color:#fff}
.mark-dot{display:inline-block;border-radius:50%;background:var(--blue);vertical-align:middle;margin-left:6px}
.contact{font-size:7px;line-height:11px;color:var(--ink);white-space:nowrap}
.contact--white{color:#fff}
.contact .ico{display:inline-block;width:5px;height:5px;border-radius:50%;background:var(--blue);margin-right:4px;vertical-align:middle}
.contact--white .ico{background:#fff}
.ghost-name{position:absolute;font-weight:900;color:var(--ghost);white-space:nowrap}
.band{position:absolute;left:0;width:100%}

/* letterhead */
.letterhead{left:36px;top:36px;width:533px;height:660px}
.letterhead .brand{position:absolute;left:18px;top:20px;font-size:30px}
.letterhead .contact{position:absolute;left:410px;top:12px}
.letterhead .ghost-name{left:60px;top:270px;font-size:70px}
.letterhead .band{bottom:0;height:120px}

/* business card front */
.card-front{left:833px;top:41px;width:360px;height:175px}
.card-front .band{top:0;height:175px}
.card-front .holder{position:absolute;left:26px;top:76px}
.card-front .holder-name{font-size:13px;font-weight:700;color:var(--blue)}
.card-front .holder-role{font-size:8px;color:var(--ink);margin-top:2px}
.card-front .contact{position:absolute;left:262px;top:44px}

/* business card backs */
.card-silver{left:734px;top:250px;width:221px;height:106px;background:linear-gradient(180deg,var(--silver-a),var(--silver-b))}
.card-silver .brand{position:absolute;left:28px;top:38px;font-size:20px}
.card-silver .web{position:absolute;left:0;right:0;bottom:10px;text-align:center;font-size:6px}
.card-blue{left:965px;top:250px;width:228px;height:106px;background:radial-gradient(ellipse at 50% 45%,var(--blue-light),var(--blue-deep))}
.card-blue .brand{position:absolute;left:30px;top:38px;font-size:20px}

/* envelope */
.envelope{left:590px;top:408px;width:603px;height:384px}
.envelope .flap{top:0;height:80px}
.envelope .flap-name{position:absolute;left:0;right:0;top:22px;text-align:center;font-size:22px}
.envelope .return{position:absolute;left:14px;top:100px}
.envelope .return .brand{font-size:24px}
.envelope .return .contact{margin-top:6px}
.envelope .ghost-name{left:290px;top:198px;font-size:44px}
.envelope .contact.lower{position:absolute;left:14px;top:268px}
.envelope .band.bottom{bottom:0;height:110px}
</style>
</head>
<body>
<main class="canvas">

  <section class="sheet letterhead" aria-label="Letterhead">
    <div class="brand">CareRally482<span class="mark-dot" style="width:14px;height:14px"></span></div>
    <div class="contact">
      20415 E Ridge Ave Suite 230-519<br>Harlow Springs, NM 85261<br>
      <span class="ico"></span>(555) 301-0110<br>
      <span class="ico"></span>(555) 301-0122<br>
      <span class="ico"></span>(555) 302-0139<br>
      <span class="ico"></span>gph@carerally482.com<br>
      <span class="ico"></span>www.carerally482.com
    </div>
    <div class="ghost-name">CareRally482</div>
    <svg class="band" viewBox="0 0 533 120" preserveAspectRatio="none" aria-hidden="true">
      <defs><linearGradient id="lhBlue" x1="0" y1="0" x2="1" y2="0"><stop offset="0" stop-color="#163c95"/><stop offset=".5" stop-color="#3f74de"/><stop offset="1" stop-color="#163c95"/></linearGradient></defs>
      <path d="M0 40 C160 95 360 70 533 10 L533 120 L0 120Z" fill="url(#lhBlue)"/>
      <path d="M0 28 C160 85 360 60 533 0 L533 10 C360 70 160 95 0 40Z" fill="#c3c6cc"/>
    </svg>
  </section>

  <section class="sheet card-front" aria-label="Business card front">
    <svg class="band" viewBox="0 0 360 175" preserveAspectRatio="none" aria-hidden="true">
      <defs><linearGradient id="cfBlue" x1="0" y1="0" x2="1" y2="1"><stop offset="0" stop-color="#3f74de"/><stop offset="1" stop-color="#163c95"/></linearGradient></defs>
      <path d="M240 0 L360 0 L360 175 L250 175 C225 120 225 50 240 0Z" fill="url(#cfBlue)"/>
      <path d="M230 0 L240 0 C225 50 225 120 250 175 L242 175 C215 120 215 50 230 0Z" fill="#c3c6cc"/>
      <path d="M0 12 C80 2 170 2 240 0 L0 0Z" fill="#c3c6cc"/>
    </svg>
    <div class="holder">
      <div class="holder-name">Gordon P. Hartwell</div>
      <div class="holder-role">Owner</div>
    </div>
    <div class="contact contact--white">
      20415 E Ridge Ave<br>Suite 230-519<br>Harlow Springs, NM<br>85261<br>
      <span class="ico"></span>(555) 301-0110<br>
      <span class="ico"></span>(555) 302-0139<br>
      <span class="ico"></span>gph@carerally482.com<br>
      <span class="ico"></span>www.carerally482.com
    </div>
  </section>

  <section class="sheet card-silver" aria-label="Business card back, silver">
    <div class="brand">CareRally482<span class="mark-dot" style="width:10px;height:10px"></span></div>
    <div class="web">www.carerally482.com</div>
  </section>

  <section class="sheet card-blue" aria-label="Business card back, blue">
    <div class="brand brand--white">CareRally482</div>
  </section>

  <section class="sheet envelope" aria-label="Envelope">
    <svg class="band flap" viewBox="0 0 603 80" preserveAspectRatio="none" aria-hidden="true">
      <defs><linearGradient id="envBlue" x1="0" y1="0" x2="1" y2="0"><stop offset="0" stop-color="#163c95"/><stop offset=".5" stop-color="#3f74de"/><stop offset="1" stop-color="#163c95"/></linearGradient></defs>
      <path d="M0 0 L603 0 L603 70 C420 50 180 50 0 70Z" fill="url(#envBlue)"/>
      <path d="M0 70 C180 50 420 50 603 70 L603 76 C420 57 180 57 0 76Z" fill="#c3c6cc"/>
    </svg>
    <div class="flap-name brand brand--white">CareRally482</div>
    <div class="return">
      <div class="brand">CareRally482<span class="mark-dot" style="width:12px;height:12px"></span></div>
      <div class="contact">20415 E Ridge Ave Suite 230-519<br>Harlow Springs, NM 85261</div>
    </div>
    <div class="ghost-name">CareRally482</div>
    <div class="contact lower">
      <span class="ico"></span>(555) 301-0110<br>
      <span class="ico"></span>(555) 301-0122<br>
      <span class="ico"></span>(555) 302-0139<br>
      <span class="ico"></span>gph@carerally482.com<br>
      <span class="ico"></span>www.carerally482.com
    </div>
    <svg class="band bottom" viewBox="0 0 603 110" preserveAspectRatio="none" aria-hidden="true">
      <path d="M0 60 C200 105 420 80 603 20 L603 110 L0 110Z" fill="url(#envBlue)"/>
      <path d="M0 50 C200 95 420 70 603 8 L603 20 C420 80 200 105 0 60Z" fill="#c3c6cc"/>
    </svg>
  </section>

</main>
</body>
</html>
```